Commercial photographer, UAV drone photography & 360 walk-through visuals

I need a business card design that is minimalist but yet pretentiously creative. My target market are architects, designers, advertising agents and marketing managers. It is important to stress that though I am asking for a minimalist design it needs to have creative impact.

Target Market(s)

Architects, interiors designers, web-designers, artists

Contact Information for Business Card

Include my name, mobile [cell] number, email, web page and the company logo. Do not to include a postal address.

Colors

Designer to choose colors to be used in the design.

Requirements
Must have
• The following information is to be included:
• Miles Perrow
• Photographer
• m: 07812 593174
• e: miles@mpframeworks.co.uk
• w: mpframeworks.co.uk

```html
<!DOCTYPE html>
<html lang="en">
<head>
<meta charset="utf-8">
<title>MP Frameworks — Business Card</title>
<link href="https://fonts.googleapis.com/css2?family=Josefin+Sans:wght@300;400;600&display=swap" rel="stylesheet">
<style>
  :root {
    --backdrop: #8e8e8e;
    --card-dark: #262626;
    --card-light: #e4e4e4;
    --ink-dark: #262626;
    --ink-light: #f2f2f2;
    --frame-light: #e8e8e8;
  }
  * { margin: 0; padding: 0; box-sizing: border-box; }
  html, body {
    width: 1200px; height: 720px; overflow: hidden;
    background: var(--backdrop);
    font-family: "Josefin Sans", sans-serif;
  }
  .canvas {
    position: relative; width: 1200px; height: 720px;
  }
  .card {
    position: absolute; top: 229px;
    width: 464px; height: 262px; overflow: hidden;
  }

  /* Back of card */
  .card--back {
    left: 112px;
    background: var(--card-dark);
  }
  .card--back .inner-frame {
    position: absolute; inset: 11px;
    border: 2px solid var(--frame-light);
  }
  .card--back .brand {
    position: absolute; left: 0; right: 0; top: 50%;
    transform: translateY(-50%);
    display: flex; align-items: center; justify-content: center; gap: 12px;
    color: var(--ink-light);
  }
  .brand-mark {
    display: block; width: 12px; height: 12px; background: currentColor;
  }
  .card--back .brand-name {
    font-size: 26px; font-weight: 400; letter-spacing: 2px;
  }

  /* Front of card */
  .card--front {
    left: 624px;
    background: var(--card-light);
    border: 6px solid var(--ink-dark);
    color: var(--ink-dark);
  }
  .card--front .brand {
    position: absolute; left: 20px; top: 38px;
    display: flex; align-items: center; gap: 6px;
  }
  .card--front .brand-mark { width: 8px; height: 8px; }
  .card--front .brand-name {
    font-size: 12px; font-weight: 400; letter-spacing: 1px;
  }
  .person {
    position: absolute; left: 20px; top: 112px;
  }
  .person-name {
    font-size: 16px; font-weight: 600; letter-spacing: 1px;
  }
  .person-role {
    font-size: 10px; font-weight: 400; letter-spacing: 0.5px; margin-top: 2px;
  }
  .contact {
    position: absolute; left: 20px; top: 162px;
    list-style: none; font-size: 12.5px; font-weight: 400; line-height: 19px;
  }
  .edge-accent {
    position: absolute; right: -40px; top: 58px;
  }
</style>
</head>
<body>
<main class="canvas">

  <section class="card card--back" aria-label="Card back">
    <div class="inner-frame"></div>
    <div class="brand">
      <span class="brand-mark"></span>
      <span class="brand-name">MP FRAMEWORKS</span>
    </div>
  </section>

  <section class="card card--front" aria-label="Card front">
    <div class="brand">
      <span class="brand-mark"></span>
      <span class="brand-name">MP FRAMEWORKS</span>
    </div>

    <div class="person">
      <p class="person-name">JOHN SMITH</p>
      <p class="person-role">TITTLE/POSTION</p>
    </div>

    <ul class="contact">
      <li>P : 123-456-7890</li>
      <li>E : email@company.com</li>
      <li>W : www.companyname.com</li>
    </ul>

    <svg class="edge-accent" width="120" height="130" viewBox="0 0 120 130" aria-hidden="true">
      <circle cx="60" cy="65" r="60" fill="var(--ink-dark)"/>
    </svg>
  </section>

</main>
</body>
</html>
```